Website for our 3rd party logistics warehouse company

Our company is a 3rd party logistics company. We receive and ship other businesses products for them. We offer our services to other smaller businesses that do not have a warehouse to operate out of. We also help many Brindlemart businesses prepare their products to be sold on Brindlemart.

We are looking for a modern looking design for our website. Please see our attached logo for design ideas. We are open to changing logo colors for website.

We really like the look of the website www.quorvane.com

Target Market(s)

Other businesses and brands of products

Industry/Entity Type

Warehousing and shipping

Number of Pages Required

2 page

Requirements
Must have
• We need 2 pages. Our main landing page and a duplicate page with different information geared towards brands.
Nice to have
• I like the look of overlay/transparent sections. Please see quorvane.com there is a ribbon that shows "Partners".

```html
<!DOCTYPE html>
<html lang="en">
<head>
<meta charset="utf-8">
<title>Corvalis 3PL</title>
<link rel="stylesheet" href="https://fonts.googleapis.com/css2?family=Montserrat:wght@500;600;700;800&family=Open+Sans:wght@300;400;600&display=swap">
<style>
:root{
  --gold:#fbb829;
  --ink:#1d1d1f;
  --body:#2a2a2a;
  --cream:#fdf6e6;
  --navy:#2a2c37;
  --footer:#1c1d23;
  --line:#e3e3e3;
  --white:#ffffff;
}
*{margin:0;padding:0;box-sizing:border-box}
html,body{width:1200px;height:3422px;overflow:hidden}
body{font-family:"Open Sans",sans-serif;color:var(--body);background:var(--white);position:relative}
section,header,footer{position:absolute;left:0;width:1200px}
.heading{font-family:"Montserrat",sans-serif;font-weight:800;color:var(--ink);letter-spacing:.5px}
.heading span{color:var(--gold)}
.brand{font-family:"Montserrat",sans-serif;font-weight:700;font-size:24px;letter-spacing:2px;color:var(--white);display:flex;align-items:center;gap:10px}
.brand i{display:block;width:12px;height:12px;border-radius:50%;background:var(--gold)}
.nav{display:flex;gap:0;font-family:"Montserrat",sans-serif;font-weight:600;font-size:14px;color:var(--white);position:absolute}
.nav a{color:inherit;text-decoration:none;position:absolute;white-space:nowrap}
.nav a.active{color:var(--gold)}

/* hero */
.hero{top:0;height:647px;background:linear-gradient(180deg,#4a4a50 0%,#6b5a4a 40%,#3a3230 70%,#23222a 100%)}
.hero .photo{position:absolute;inset:0}
.hero .brand{position:absolute;left:130px;top:60px}
.hero .nav{left:0;top:36px}
.hero h1{position:absolute;top:452px;width:100%;text-align:center;font-size:42px;color:var(--white)}
.hero p{position:absolute;top:524px;left:250px;width:700px;text-align:center;font-size:17px;line-height:29px;color:#f0f0f0}

/* why */
.why{top:647px;height:449px}
.why h2{position:absolute;top:64px;width:100%;text-align:center;font-size:28px}
.why .col{position:absolute;top:160px;height:236px;text-align:center;font-size:15px;line-height:22.5px;color:#222}
.why .col svg{display:block;margin:20px auto 28px}
.why .divider{position:absolute;top:160px;width:1px;height:236px;background:var(--line)}

/* benefits */
.benefits{top:1096px;height:565px;background:var(--cream)}
.benefits h2{position:absolute;top:70px;width:100%;text-align:center;font-size:28px}
.benefits .photo{position:absolute;left:0;top:167px;width:647px;height:398px;background:linear-gradient(160deg,#5b6270 0%,#8c93a0 40%,#e6e7ea 62%,#9a9ea6 100%)}
.benefit{position:absolute;left:693px;display:flex;align-items:center;gap:20px;font-family:"Montserrat",sans-serif;font-weight:500;font-size:15px;line-height:23px;color:#222}
.benefit .badge{width:58px;height:58px;border-radius:50%;background:var(--gold);display:flex;align-items:center;justify-content:center;flex:none}

/* software */
.software{top:1661px;height:591px}
.software h2{position:absolute;left:130px;top:126px;font-size:28px}
.software p{position:absolute;left:130px;top:233px;width:390px;font-size:20px;line-height:33.5px;font-weight:300;color:#222}
.software .screen{position:absolute;left:560px;top:60px;width:640px;height:470px;background:radial-gradient(ellipse at 55% 40%,#eef0f6 0%,#dfe2ea 45%,#ffffff 80%)}

/* guarantee */
.guarantee{top:2252px;height:471px;background:var(--cream)}
.guarantee .photo{position:absolute;left:0;top:0;width:609px;height:471px;background:linear-gradient(150deg,#6f5a3e 0%,#a5673a 35%,#3d4a63 70%,#262a33 100%)}
.guarantee h2{position:absolute;left:666px;top:84px;font-size:28px}
.guarantee p{position:absolute;left:666px;top:176px;width:410px;font-size:20px;line-height:33.5px;font-weight:300;color:#222}

/* contact */
.contact{top:2723px;height:541px;background:linear-gradient(180deg,#2f313c 0%,#2a2c37 60%,#33302f 100%)}
.contact .photo{position:absolute;inset:0}
.contact h2{position:absolute;top:80px;width:100%;text-align:center;font-size:28px;color:var(--white)}
.field{position:absolute;background:var(--white);border-radius:6px;font-size:13px;color:#555;padding:14px 16px}
.submit{position:absolute;left:526px;top:3170px;width:148px;height:50px;border-radius:6px;background:var(--gold);font-family:"Montserrat",sans-serif;font-weight:800;font-size:18px;color:#1c1c1c;display:flex;align-items:center;justify-content:center}

/* footer */
.site-footer{top:3264px;height:158px;background:var(--footer)}
.site-footer .brand{position:absolute;left:130px;top:84px;font-size:22px}
.site-footer .nav{left:0;top:56px}
.copyright{position:absolute;right:132px;top:97px;font-size:12px;color:#e8e8e8}
</style>
</head>
<body>

<header class="hero">
  <div class="photo" role="img" aria-label="Red semi truck with trailer on a desert highway at dusk"></div>
  <div class="brand"><i></i>CORVALIS 3PL</div>
  <nav class="nav">
    <a class="active" style="left:535px">HOME</a>
    <a style="left:618px">ABOUT US</a>
    <a style="left:741px">BENEFITS</a>
    <a style="left:859px">SOFTWARE</a>
    <a style="left:979px">CONTACT US</a>
  </nav>
  <h1 class="heading" style="color:#fff">WHO <span>WE ARE</span></h1>
  <p>Corvalis 3PL is your one stop 3PL that will help you grow your business and allow you to be handsoff. We offer high end services and meet our commitment, guaranteed.</p>
</header>

<section class="why">
  <h2 class="heading">WHY USE A <span>PREP 3PL?</span></h2>
  <div class="col" style="left:130px;width:152px">
    <svg width="84" height="84" viewBox="0 0 84 84" fill="none" stroke="#333" stroke-width="2">
      <circle cx="42" cy="42" r="36"/><circle cx="42" cy="42" r="24" stroke="#fbb829"/>
      <path d="M30 34c6 2 8-4 14-2s4 8 10 8M28 50c6-2 10 4 16 2" stroke="#fbb829"/>
      <circle cx="42" cy="6" r="4" fill="#fff"/><circle cx="42" cy="78" r="4" fill="#fff"/><circle cx="6" cy="42" r="4" fill="#fff"/><circle cx="78" cy="42" r="4" fill="#fff"/>
    </svg>
    Work from anywhere in the world
  </div>
  <div class="divider" style="left:318px"></div>
  <div class="col" style="left:345px;width:200px">
    <svg width="84" height="84" viewBox="0 0 84 84" fill="none" stroke="#333" stroke-width="2">
      <path d="M36 6h12l2 10 8 4 9-6 8 8-6 9 4 8 10 2v12l-10 2-4 8 6 9-8 8-9-6-8 4-2 10H36l-2-10-8-4-9 6-8-8 6-9-4-8-10-2V36l10-2 4-8-6-9 8-8 9 6 8-4z"/>
      <circle cx="42" cy="42" r="16" stroke="#fbb829"/>
    </svg>
    Don't have to manage employees, health insurance plans, payroll, sick calls, etc
  </div>
  <div class="divider" style="left:579px"></div>
  <div class="col" style="left:615px;width:222px">
    <svg width="84" height="84" viewBox="0 0 84 84" fill="none" stroke="#333" stroke-width="2">
      <path d="M20 8h50v8M20 8c-5 0-5 8 0 8h10M24 16v58H12c-5 0-5-8 0-8h12M24 74h30M66 16v30"/>
      <path d="M34 26h24M34 34h24M34 42h18M34 50h14" stroke="#fbb829"/>
      <circle cx="62" cy="58" r="8"/><path d="M58 65v12l4-3 4 3V65"/>
    </svg>
    Don't get locked into a 3-5 year warehouse lease where you guarantee hundreds of thousands of dollars
  </div>
  <div class="divider" style="left:876px"></div>
  <div class="col" style="left:900px;width:170px">
    <svg width="84" height="84" viewBox="0 0 84 84" fill="none" stroke="#333" stroke-width="2">
      <rect x="6" y="8" width="72" height="66"/><path d="M6 18h72M62 13h2M68 13h2M74 13h2"/>
      <path d="M22 62V46h10v16M38 62V36h10v26M54 62V28h10v34" stroke="#fbb829"/>
      <path d="M18 38l12-10 8 4 14-12" stroke="#fbb829"/>
    </svg>
    Grow your business without commitment
  </div>
</section>

<section class="benefits">
  <h2 class="heading">OUR <span>BENEFITS</span></h2>
  <div class="photo" role="img" aria-label="White delivery truck parked at a warehouse loading dock"></div>
  <div class="benefit" style="top:164px">
    <div class="badge"><svg width="32" height="32" viewBox="0 0 32 32" fill="none" stroke="#fff" stroke-width="2.2"><circle cx="16" cy="16" r="13"/><path d="M16 8v8l6 4"/></svg></div>
    <div>48 hour turn around guarantee –<br>done in 48 hours or its free*</div>
  </div>
  <div class="benefit" style="top:241px">
    <div class="badge"><svg width="32" height="32" viewBox="0 0 32 32" fill="none" stroke="#fff" stroke-width="2.2"><circle cx="16" cy="10" r="7"/><path d="M3 24l6-4h8l6 2 6-4M3 29h18l8-6"/></svg></div>
    <div>No monthly subscription –<br>only pay for what you use</div>
  </div>
  <div class="benefit" style="top:321px">
    <div class="badge"><svg width="32" height="32" viewBox="0 0 32 32" fill="none" stroke="#fff" stroke-width="2.2"><path d="M4 18h7l2 4h6l2-4h7v10H4zM4 18l4-8M28 18l-4-8M16 3v12M11 10l5 5 5-5"/></svg></div>
    <div>No receiving fees</div>
  </div>
  <div class="benefit" style="top:399px">
    <div class="badge"><svg width="32" height="32" viewBox="0 0 32 32" fill="none" stroke="#fff" stroke-width="2.2"><circle cx="16" cy="12" r="7"/><circle cx="16" cy="12" r="2.5"/><path d="M3 18l5 10M29 18l-5 10M8 28h16"/></svg></div>
    <div>No pallet or outbound fees</div>
  </div>
  <div class="benefit" style="top:475px">
    <div class="badge"><svg width="32" height="32" viewBox="0 0 32 32" fill="none" stroke="#fff" stroke-width="2.2"><path d="M6 18v-3a10 10 0 0120 0v3"/><rect x="4" y="17" width="5" height="8" rx="2"/><rect x="23" y="17" width="5" height="8" rx="2"/><path d="M26 25c0 3-4 4-8 4"/></svg></div>
    <div>Email and phone support</div>
  </div>
</section>

<section class="software">
  <h2 class="heading">OUR <span>SOFTWARE</span></h2>
  <p>Know what inventory is at our warehouse in real time. Our software allows you to track your inventory and know how your shipment status in real time. Professional software designed specifically for our needs.</p>
  <div class="screen" role="img" aria-label="Desktop monitor showing an inventory dashboard with charts"></div>
</section>

<section class="guarantee">
  <div class="photo" role="img" aria-label="Warehouse workers moving boxes between tall pallet racks"></div>
  <h2 class="heading">OUR <span>GUARANTEE</span></h2>
  <p>All orders will be prepped and ready for shipment in 48 business hours (often 24 or less) and we guarantee it. We are confident in our services and if we do not fulfill our obligation, we offer a 500 item (up to $700) credit on your next shipment.</p>
</section>

<section class="contact">
  <div class="photo" role="img" aria-label="Shipping containers stacked at a port at dusk"></div>
  <h2 class="heading" style="color:#fff">CONTACT <span>US</span></h2>
</section>
<div class="field" style="left:303px;top:2912px;width:292px;height:46px">First Name</div>
<div class="field" style="left:606px;top:2912px;width:292px;height:46px">Last Name</div>
<div class="field" style="left:303px;top:2976px;width:292px;height:46px">Phone</div>
<div class="field" style="left:606px;top:2976px;width:292px;height:46px">Email</div>
<div class="field" style="left:303px;top:3040px;width:595px;height:102px">Message</div>
<div class="submit">SUBMIT</div>

<footer class="site-footer">
  <div class="brand"><i></i>CORVALIS 3PL</div>
  <nav class="nav">
    <a style="left:563px">HOME</a>
    <a style="left:641px">ABOUT US</a>
    <a style="left:758px">BENEFITS</a>
    <a style="left:869px">SOFTWARE</a>
    <a style="left:983px">CONTACT US</a>
  </nav>
  <div class="copyright">Copyright © 2021 All Rights Reserved</div>
</footer>

</body>
</html>
```